依頼詳細
ページに使用したいキャッチフレーズ:
個性的な道を究め、劇的に生きる人生を選択する
それがMoonhollow

参考にしたいURL:
https://www.kenmori-ux.brelo.jp/
https://www.sorimachikeigo.com/member-lounge

ムーンホロウクラブのHP:
https://www.ruvo.co.jp/moonhollow/

ページに使用したいテキスト:
『Moonhollow Clubとは

「あなたの好きなことは何ですか?」
好きなことを徹底追求し、“好き”を個性に。
そして、個性を武器にしながら“才能”へと伸ばしていくことで、
人生の構想力が磨かれ、あなたの人生は切り拓かれていきます。

誰かに敷かれたレールに乗りたいのか?
型にはまらない人生を創造したいのか?
一度きりの人生を、自分はどう生きたいか?

「自分らしい」人生を実現しよう!。』

採択後、デザインに利用した、デザインデータもお送りください。
(特に、画像ファイルは必ず送ってください)

何かご不明な点がございましたら、お気軽にお申し付けください。

※ 過去の制作実績をそのままご提案いただいたり、他社のポートフォリオをそのまま掲載することは恐れ入りますが、ご遠慮いただけますと幸いです。
サイトURL
http://moonhollowclub.jp
ページ数
1ページ
希望イメージ
シンプル 複雑
単色 カラフル
暗い 明るい
日常 高級
遊び心 厳粛
未来的 伝統的
女性的 男性的
希望する色
赤系、黄・オレンジ系、ジェンダーニュートラルなデザイン
納品ファイル
• イラストレーター形式 (.ai)
• PNG形式 (.png)
補足説明
デザインに利用した、デザインデータ(画像など)もお送り頂きますようお願い致します。

素晴らしいデザインをありがとうございました。

素晴らしいデザインをありがとうございました。

```html
<!DOCTYPE html>
<html lang="ja">
<head>
<meta charset="UTF-8">
<title>Moonhollow Club</title>
<link href="https://fonts.googleapis.com/css2?family=Noto+Sans+JP:wght@400;500;700;900&family=Montserrat:wght@700;800&family=Playfair+Display:wght@700&display=swap" rel="stylesheet">
<style>
:root{
  --red:#e50f2b;
  --red-deep:#c8001f;
  --orange:#ff6a3d;
  --orange-soft:#ff8a4c;
  --ink:#1e1e1e;
  --muted:#666;
  --line:#e6e6e6;
  --black:#0d0d0d;
  --white:#fff;
}
*{box-sizing:border-box;margin:0;padding:0}
html,body{width:1200px;height:3052px;overflow:hidden}
body{position:relative;font-family:"Noto Sans JP",sans-serif;color:var(--ink);background:var(--white)}
.abs{position:absolute}

/* header */
.site-header{position:absolute;top:0;left:0;width:1200px;height:80px;background:var(--white);z-index:5}
.brand{position:absolute;left:26px;top:16px}
.brand-name{font-family:"Montserrat",sans-serif;font-weight:800;font-size:26px;color:var(--red);letter-spacing:.5px}
.brand-tag{font-size:10px;color:var(--ink);margin-top:2px}
.global-nav{position:absolute;left:690px;top:30px;display:flex;gap:30px;font-size:13px;font-weight:700}
.menu-btn{position:absolute;right:26px;top:20px;width:40px;text-align:center;color:var(--red);font-family:"Montserrat",sans-serif;font-size:10px;font-weight:700}
.menu-btn span{display:block;height:3px;background:var(--red);margin-bottom:5px;border-radius:2px}

/* hero */
.hero{position:absolute;top:80px;left:0;width:1200px;height:720px;overflow:hidden}
.hero-panel{position:absolute;left:0;top:0;width:600px;height:720px;background:linear-gradient(160deg,#f2243b,var(--red-deep))}
.hero-photo{position:absolute;left:600px;top:0;width:490px;height:720px;background:linear-gradient(180deg,#b9b7b4 0%,#e9e6e2 35%,#f4f1ee 55%,#a39586 80%,#6e5a4a 100%)}
.hero-strip{position:absolute;left:1090px;top:0;width:110px;height:720px;background:var(--red)}
.hero-copy{position:absolute;left:0;top:250px;width:600px;text-align:center;color:var(--white);font-weight:700;font-size:30px;line-height:1.6}
.hero-copy .en{font-family:"Montserrat",sans-serif;font-weight:800;font-size:30px}
.join-btn{position:absolute;right:20px;top:28px;width:180px;height:44px;border-radius:22px;background:linear-gradient(90deg,var(--orange-soft),var(--orange));color:var(--white);font-size:14px;font-weight:700;text-align:center;line-height:44px;box-shadow:0 3px 8px rgba(0,0,0,.2)}
.hero-wordmark{position:absolute;left:-20px;top:590px;font-family:"Playfair Display",serif;font-size:210px;line-height:1;color:rgba(255,255,255,.08);-webkit-text-stroke:2px rgba(190,0,25,.45);white-space:nowrap}

/* about */
.about{position:absolute;top:800px;left:0;width:1200px;height:680px;background:var(--white)}
.about-deco-left{position:absolute;left:0;top:40px;width:420px;height:560px;background:radial-gradient(ellipse at 100% 50%,rgba(229,15,43,.55),rgba(229,15,43,.15) 45%,rgba(255,255,255,0) 75%)}
.about-deco-right{position:absolute;right:0;top:200px;width:320px;height:360px;background:radial-gradient(ellipse at 0% 60%,rgba(229,15,43,.5),rgba(229,15,43,.1) 50%,rgba(255,255,255,0) 80%)}
.about-card{position:absolute;left:280px;top:60px;width:640px;height:600px;background:var(--white);box-shadow:0 6px 24px rgba(0,0,0,.12);text-align:center;padding-top:54px}
.about-title{font-size:30px;font-weight:700;color:var(--red);margin-bottom:44px}
.about-title .en{font-family:"Montserrat",sans-serif;font-weight:800}
.about-text{font-size:14px;line-height:2.3;margin-bottom:30px}

/* feed sections */
.feed{position:absolute;left:0;width:1200px}
.feed-band{position:absolute;left:0;top:0;width:1200px;height:220px}
.movie .feed-band{background:linear-gradient(90deg,#d8001f,#ee2b3b 60%,#d8001f)}
.blog .feed-band{background:linear-gradient(90deg,#ff5a3a,#ff7a48 60%,#ff5a3a)}
.band-photo{position:absolute;right:0;top:0;width:700px;height:220px;opacity:.35}
.movie .band-photo{background:linear-gradient(90deg,rgba(120,0,10,0),rgba(120,0,10,.8))}
.blog .band-photo{background:linear-gradient(90deg,rgba(170,40,0,0),rgba(170,40,0,.7))}
.feed-title{position:absolute;left:80px;top:34px;color:var(--white);font-family:"Montserrat",sans-serif;font-weight:800;font-size:56px;line-height:1}
.feed-sub{position:absolute;left:82px;top:96px;color:var(--white);font-size:12px}
.more-btn{position:absolute;right:80px;top:52px;width:150px;height:40px;border-radius:20px;background:var(--white);color:var(--red);font-size:12px;font-weight:700;line-height:40px;padding-left:28px}
.more-btn svg{position:absolute;right:12px;top:10px}
.cards{position:absolute;left:80px;top:160px;display:flex;gap:40px}
.card{width:230px}
.thumb{width:230px;height:140px;background:linear-gradient(135deg,#8a6e5c,#d9c8bb 55%,#5e4a3e)}
.card-meta{display:flex;justify-content:space-between;align-items:center;margin:14px 0 10px}
.tag{border:1px solid var(--red);color:var(--red);font-size:10px;padding:2px 10px}
.date{font-size:11px;color:var(--muted);font-family:"Montserrat",sans-serif}
.card-text{font-size:12px;line-height:1.7}

/* board */
.board{position:absolute;top:2480px;left:0;width:1200px;text-align:center}
.board-title{font-size:24px;font-weight:700;margin-bottom:16px}
.board-note{font-size:12px;color:var(--muted)}
.board-note a{color:var(--red);text-decoration:underline}
.search{position:relative;margin:22px auto 0;width:380px;height:44px;border:1px solid var(--line);border-radius:4px;background:#f7f7f7}
.search svg{position:absolute;right:14px;top:12px}

/* footer */
.site-footer{position:absolute;top:2720px;left:0;width:1200px;height:332px;background:var(--black);color:var(--white)}
.foot-brand{position:absolute;left:60px;top:50px}
.foot-brand .brand-name{color:var(--white)}
.foot-brand .brand-tag{color:#ccc}
.foot-btns{position:absolute;left:60px;top:140px;display:flex;gap:16px}
.foot-btn{height:40px;line-height:40px;border:1px solid var(--white);font-size:12px;text-align:center;padding:0 22px}
.foot-btn.primary{background:var(--red);border-color:var(--red)}
.foot-nav{position:absolute;right:60px;top:60px;display:flex;gap:30px;font-size:12px}
.social{position:absolute;right:60px;top:250px;display:flex;gap:18px}
.social span{width:24px;height:24px;border-radius:50%;background:var(--white)}
.copyright{position:absolute;left:60px;top:256px;font-size:11px;color:#bbb}
</style>
</head>
<body>

<header class="site-header">
  <div class="brand">
    <div class="brand-name">Moonhollow Club</div>
    <div class="brand-tag">個性的な道を究め、劇的に生きる</div>
  </div>
  <nav class="global-nav"><span>ホーム</span><span>動画</span><span>ブログ</span><span>お知らせ</span><span>お問い合わせ</span></nav>
  <div class="menu-btn"><span></span><span></span><span></span>MENU</div>
</header>

<section class="hero">
  <div class="hero-panel"></div>
  <div class="hero-photo" role="img" aria-label="霧の中へ続く線路の写真"></div>
  <div class="hero-strip"></div>
  <div class="hero-wordmark">Moonhollow Club</div>
  <div class="hero-copy">個性的な道を究め、<br>劇的に生きる人生を選択する<br>それが<br><span class="en">Moonhollow</span></div>
  <div class="join-btn">新規会員登録</div>
</section>

<section class="about">
  <div class="about-deco-left" role="img" aria-label="放射状に広がる赤いラインの装飾"></div>
  <div class="about-deco-right" role="img" aria-label="赤いラインの装飾"></div>
  <div class="about-card">
    <h2 class="about-title"><span class="en">Moonhollow Club</span> とは</h2>
    <p class="about-text">「あなたの好きなことは何ですか?」<br>好きなことを徹底追求し、“好き”を個性に。<br>そして、個性を武器にしながら“才能”へと伸ばしていくことで、<br>人生の構想力が磨かれ、あなたの人生は切り拓かれていきます。</p>
    <p class="about-text">誰かに敷かれたレールに乗りたいのか?<br>型にはまらない人生を創造したいのか?<br>一度きりの人生を、自分はどう生きたいか?</p>
    <p class="about-text">「自分らしい」人生を実現しよう!</p>
  </div>
</section>

<section class="feed movie" style="top:1480px;height:400px">
  <div class="feed-band"><div class="band-photo" role="img" aria-label="人々のシルエット写真"></div></div>
  <h2 class="feed-title">MOVIE</h2>
  <div class="feed-sub">新着動画</div>
  <div class="more-btn">一覧を見る<svg width="20" height="20" viewBox="0 0 20 20"><circle cx="10" cy="10" r="9" fill="var(--red)"/><path d="M7 10h6M11 7l3 3-3 3" stroke="#fff" stroke-width="1.6" fill="none"/></svg></div>
  <div class="cards">
    <article class="card"><div class="thumb" role="img" aria-label="キーボードを打つ手元の写真"></div><div class="card-meta"><span class="tag">ドキュメンタリー</span><span class="date">2023.06.06</span></div><p class="card-text">ダミーテキスト。本文はすべて仮の内容です。あとからここは差し替え予定です。</p></article>
    <article class="card"><div class="thumb" role="img" aria-label="キーボードを打つ手元の写真"></div><div class="card-meta"><span class="tag">ドキュメンタリー</span><span class="date">2023.06.06</span></div><p class="card-text">ダミーテキスト。本文はすべて仮の内容です。あとからここは差し替え予定です。</p></article>
    <article class="card"><div class="thumb" role="img" aria-label="キーボードを打つ手元の写真"></div><div class="card-meta"><span class="tag">ドキュメンタリー</span><span class="date">2023.06.06</span></div><p class="card-text">ダミーテキスト。本文はすべて仮の内容です。あとからここは差し替え予定です。</p></article>
    <article class="card"><div class="thumb" role="img" aria-label="キーボードを打つ手元の写真"></div><div class="card-meta"><span class="tag">ドキュメンタリー</span><span class="date">2023.06.06</span></div><p class="card-text">ダミーテキスト。本文はすべて仮の内容です。あとからここは差し替え予定です。</p></article>
  </div>
</section>

<section class="feed blog" style="top:1880px;height:560px">
  <div class="feed-band"><div class="band-photo" role="img" aria-label="作業風景の写真"></div></div>
  <h2 class="feed-title">BLOG</h2>
  <div class="feed-sub">ブログ</div>
  <div class="more-btn">一覧を見る<svg width="20" height="20" viewBox="0 0 20 20"><circle cx="10" cy="10" r="9" fill="var(--red)"/><path d="M7 10h6M11 7l3 3-3 3" stroke="#fff" stroke-width="1.6" fill="none"/></svg></div>
  <div class="cards">
    <article class="card"><div class="thumb" role="img" aria-label="ノートパソコンで作業する手元の写真"></div><div class="card-meta"><span class="tag">ドキュメンタリー</span><span class="date">2023.06.06</span></div><p class="card-text">ダミーテキスト。本文はすべて仮の内容です。あとからここは差し替え予定です。</p></article>
    <article class="card"><div class="thumb" role="img" aria-label="ノートパソコンで作業する手元の写真"></div><div class="card-meta"><span class="tag">ドキュメンタリー</span><span class="date">2023.06.06</span></div><p class="card-text">ダミーテキスト。本文はすべて仮の内容です。あとからここは差し替え予定です。</p></article>
    <article class="card"><div class="thumb" role="img" aria-label="ノートパソコンで作業する手元の写真"></div><div class="card-meta"><span class="tag">ドキュメンタリー</span><span class="date">2023.06.06</span></div><p class="card-text">ダミーテキスト。本文はすべて仮の内容です。あとからここは差し替え予定です。</p></article>
    <article class="card"><div class="thumb" role="img" aria-label="ノートパソコンで作業する手元の写真"></div><div class="card-meta"><span class="tag">ドキュメンタリー</span><span class="date">2023.06.06</span></div><p class="card-text">ダミーテキスト。本文はすべて仮の内容です。あとからここは差し替え予定です。</p></article>
  </div>
</section>

<section class="board">
  <h2 class="board-title">掲示板</h2>
  <p class="board-note">チャットルームを利用するには、<a>ログイン</a>してください。</p>
  <div class="search"><svg width="20" height="20" viewBox="0 0 20 20"><circle cx="8" cy="8" r="6" stroke="#333" stroke-width="2" fill="none"/><path d="M12.5 12.5l5 5" stroke="#333" stroke-width="2"/></svg></div>
</section>

<footer class="site-footer">
  <div class="foot-brand">
    <div class="brand-name">Moonhollow Club</div>
    <div class="brand-tag">個性的な道を究め、劇的に生きる</div>
  </div>
  <div class="foot-btns"><div class="foot-btn primary">新規会員登録はこちら</div><div class="foot-btn">ログイン</div></div>
  <nav class="foot-nav"><span>ホーム</span><span>お知らせ</span><span>利用規約</span><span>プライバシーポリシー</span><span>運営会社</span></nav>
  <div class="copyright">© 2023 Moonhollow Club All Rights Reserved.</div>
  <div class="social" aria-label="SNSリンク"><span></span><span></span><span></span><span></span><span></span></div>
</footer>

</body>
</html>
```